Bref créative
Stationary for a Home Builder
Calvin Morrow
Professional
Calvin Morrow, MBA
Owner
4827 Pelham Crescent
Edmonton, AB
T6R 2J8
calvin@rpbbuilds.com
rpbbuilds.com
For the business card you may want to delete the 'rpbbuilds.com' at the bottom which is currently on the AI file provided.
I'd like to have the logo on the back of the card with enough white space to allow hand written notes to be added.
Logo - White and Blue - AI
Logo - White and Blue - EPS
Logo - Black and Blue - AI
Logo - Black and Blue - EPS

```html
<!DOCTYPE html>
<html lang="en">
<head>
<meta charset="utf-8">
<title>RPB Builds Stationery</title>
<link href="https://fonts.googleapis.com/css2?family=Roboto:wght@400;700&family=Roboto+Condensed:wght@400;700&display=swap" rel="stylesheet">
<style>
  :root{
    --board:#b9bbbe;
    --paper:#ffffff;
    --ink:#1d1d1f;
    --blue:#1f6fb8;
    --muted:#6b6e73;
    --rule:#c9cbce;
  }
  *{box-sizing:border-box;margin:0;padding:0}
  html,body{width:1200px;height:568px;overflow:hidden}
  body{background:var(--board);font-family:"Roboto",sans-serif;color:var(--ink);position:relative}
  .piece{position:absolute;background:var(--paper);overflow:hidden;box-shadow:0 2px 6px rgba(0,0,0,.25)}
  .label{position:absolute;font:400 9px "Roboto Condensed",sans-serif;color:#3a3c40;white-space:nowrap}
  .brand{font-family:"Roboto",sans-serif;font-weight:700;color:var(--ink);letter-spacing:-.5px;line-height:1;white-space:nowrap}
  .brand .mark{display:inline-block;background:var(--blue);vertical-align:middle;margin-right:.25em}
  .corner{position:absolute;left:0;bottom:0;width:100%;height:100%}

  /* sign */
  .sign{left:29px;top:48px;width:355px;height:504px}
  .sign .brand{position:absolute;left:26px;top:30px;font-size:54px}
  .sign .brand .mark{width:30px;height:30px}
  .sign-call{position:absolute;left:40px;top:210px;transform:rotate(-15deg);transform-origin:left top;font:700 32px/1.05 "Roboto Condensed",sans-serif}
  .sign-fields{position:absolute;left:24px;top:330px;right:24px;color:#fff;font:400 27px "Roboto Condensed",sans-serif}
  .sign-fields .row{display:flex;align-items:flex-end;gap:6px;height:42px}
  .sign-fields .line{flex:1;border-bottom:2px solid #fff;height:22px}
  .sign-url{position:absolute;right:20px;bottom:14px;color:#fff;font:700 17px "Roboto",sans-serif}

  /* letterheads */
  .letter{top:204px;width:228px;height:319px}
  .letter-a{left:427px}
  .letter-b{left:672px}
  .letter .brand{position:absolute;left:14px;top:14px;font-size:26px}
  .letter .brand .mark{width:12px;height:12px}
  .letter-contact{position:absolute;right:14px;top:16px;font-size:5.5px;line-height:1.35;color:var(--muted);text-align:left}
  .form{position:absolute;left:14px;top:62px;width:200px;border-collapse:collapse;font-size:5.5px;color:var(--muted)}
  .form td{border:1px solid var(--rule);height:11px;padding:1px 3px}
  .checks{position:absolute;left:14px;top:135px;display:flex;gap:9px;font-size:5.5px;color:var(--muted)}
  .checks span::before{content:"";display:inline-block;width:5px;height:5px;border:1px solid var(--muted);margin-right:2px;vertical-align:-1px}
  .letter-url{position:absolute;left:14px;bottom:8px;font-size:5px;color:#fff}

  /* business cards */
  .card{top:72px;width:60px;height:100px}
  .card-front{left:732px}
  .card-back{left:799px}
  .card .brand{position:absolute;left:7px;top:9px;font-size:15px}
  .card .brand .mark{width:6px;height:6px}
  .card-info{position:absolute;left:7px;top:36px;font-size:3.6px;line-height:1.45;color:var(--muted)}
  .card-back .brand{top:10px}

  /* email signature */
  .email{left:893px;top:72px;width:283px;height:79px}
  .email-info{position:absolute;left:10px;top:10px;font-size:6px;line-height:1.4;color:var(--muted)}
  .email-info b{color:var(--ink);font-size:7px}
  .email .brand{position:absolute;right:14px;top:14px;font-size:26px}
  .email .brand .mark{width:12px;height:12px}

  /* envelopes */
  .envelope{left:972px;width:204px;height:120px}
  .env-front{top:228px}
  .env-back{top:384px}
  .env-front .brand{position:absolute;left:10px;top:10px;font-size:17px}
  .env-front .brand .mark{width:8px;height:8px}
  .env-front .env-return{position:absolute;left:10px;top:32px;font-size:4.5px;line-height:1.4;color:var(--muted)}
  .env-back .brand{position:absolute;left:50%;top:66px;transform:translateX(-50%);font-size:15px}
  .env-back .brand .mark{width:7px;height:7px}
</style>
</head>
<body>

  <div class="label" style="left:165px;top:34px">Sign (24" x 36")</div>
  <section class="piece sign">
    <svg class="corner" viewBox="0 0 355 504" preserveAspectRatio="none" aria-hidden="true">
      <polygon points="0,300 280,228 280,203 355,185 355,504 0,504" fill="var(--blue)"/>
    </svg>
    <div class="brand"><span class="mark"></span>rpb builds</div>
    <div class="sign-call">Calls Us Today<br>780.555.0164</div>
    <div class="sign-fields">
      <div class="row">Address<span class="line"></span></div>
      <div class="row">Lot<span class="line"></span>Block<span class="line"></span></div>
      <div class="row">Job #<span class="line"></span></div>
    </div>
    <div class="sign-url">rpbbuilds.com</div>
  </section>

  <div class="label" style="left:520px;top:190px">Work Order</div>
  <section class="piece letter letter-a">
    <svg class="corner" viewBox="0 0 228 319" preserveAspectRatio="none" aria-hidden="true">
      <polygon points="0,300 200,300 228,285 228,319 0,319" fill="var(--blue)"/>
    </svg>
    <div class="brand"><span class="mark"></span>rpb builds</div>
    <div class="letter-contact">4827 Pelham Crescent<br>Edmonton, AB T6R 2J8<br>780.555.0164<br>calvin@rpbbuilds.com</div>
    <table class="form">
      <tr><td>Date</td><td></td><td>Name</td><td></td></tr>
      <tr><td>Phone</td><td></td><td>Lot</td><td></td></tr>
      <tr><td>Block</td><td></td><td>Job</td><td></td></tr>
      <tr><td></td><td></td><td></td><td></td></tr>
      <tr><td></td><td></td><td></td><td></td></tr>
    </table>
    <div class="checks"><span>Framing</span><span>Electrical</span><span>Plumbing</span><span>Finishing</span></div>
    <div class="letter-url">rpbbuilds.com</div>
  </section>

  <div class="label" style="left:765px;top:190px">Letterhead</div>
  <section class="piece letter letter-b">
    <svg class="corner" viewBox="0 0 228 319" preserveAspectRatio="none" aria-hidden="true">
      <polygon points="0,300 200,300 228,285 228,319 0,319" fill="var(--blue)"/>
    </svg>
    <div class="brand"><span class="mark"></span>rpb builds</div>
    <div class="letter-contact">4827 Pelham Crescent<br>Edmonton, AB T6R 2J8<br>780.555.0164<br>calvin@rpbbuilds.com</div>
    <div class="letter-url">rpbbuilds.com</div>
  </section>

  <div class="label" style="left:736px;top:58px">Card Front</div>
  <section class="piece card card-front">
    <svg class="corner" viewBox="0 0 60 100" preserveAspectRatio="none" aria-hidden="true">
      <polygon points="0,92 45,84 45,80 60,77 60,100 0,100" fill="var(--blue)"/>
    </svg>
    <div class="brand"><span class="mark"></span>rpb</div>
    <div class="card-info"><b>Calvin Morrow, MBA</b><br>Owner<br>4827 Pelham Crescent<br>Edmonton, AB<br>T6R 2J8<br>calvin@rpbbuilds.com</div>
  </section>

  <div class="label" style="left:805px;top:58px">Card Back</div>
  <section class="piece card card-back">
    <svg class="corner" viewBox="0 0 60 100" preserveAspectRatio="none" aria-hidden="true">
      <polygon points="0,92 45,84 45,80 60,77 60,100 0,100" fill="var(--blue)"/>
    </svg>
    <div class="brand"><span class="mark"></span>rpb</div>
  </section>

  <div class="label" style="left:1005px;top:58px">Email Signature</div>
  <section class="piece email">
    <svg class="corner" viewBox="0 0 283 79" preserveAspectRatio="none" aria-hidden="true">
      <polygon points="120,79 230,68 230,62 283,56 283,79" fill="var(--blue)"/>
    </svg>
    <div class="email-info"><b>Calvin Morrow, MBA</b><br>Owner<br>780.555.0164<br>calvin@rpbbuilds.com<br>rpbbuilds.com</div>
    <div class="brand"><span class="mark"></span>rpb builds</div>
  </section>

  <div class="label" style="left:1045px;top:214px">Envelope Front</div>
  <section class="piece envelope env-front">
    <svg class="corner" viewBox="0 0 204 120" preserveAspectRatio="none" aria-hidden="true">
      <polygon points="120,120 175,110 175,105 204,100 204,120" fill="var(--blue)"/>
    </svg>
    <div class="brand"><span class="mark"></span>rpb builds</div>
    <div class="env-return">4827 Pelham Crescent<br>Edmonton, AB T6R 2J8</div>
  </section>

  <div class="label" style="left:1045px;top:370px">Envelope Back</div>
  <section class="piece envelope env-back">
    <svg class="corner" viewBox="0 0 204 120" preserveAspectRatio="none" aria-hidden="true">
      <polyline points="0,0 102,58 204,0" fill="none" stroke="var(--rule)" stroke-width="1"/>
    </svg>
    <div class="brand"><span class="mark"></span>rpb builds</div>
  </section>

</body>
</html>
```